Harbour Press website re-design

We would like to recreate the www.harbourpress.example.au website into a simpler and more sophisticated version. We want the buyer to be drawn to our site and establish that we are reputable and professional from the moment they enter. We want them to easily find the product or service they are looking for within our site, decide that they would like to find out more and either click through to obtain a quote or click through to contact a rep.

The current website has been created using MS Front Page, however we would like the newly designed site to be created in a mobile responsive WordPress CMS format

We are a Print Broker who can save clients time in hunting around for the right supplier for their print jobs. This is most likely appealing to larger organisations who haven’t got time to waste in finding quotes from many different suppliers for each type of job. We make it easy because we have access to a large network of trade only print & signage suppliers so we can select the best and most cost effective supplier depending on the type of print job. Further, because we don’t do the printing in-house we have low overheads which means we can ensure competitive prices.
Updates

Target Market(s)

Business owners, print managers, receptionists, marketing managers who are time poor, uneducated re:printing, after quick & cost effective solutions

Industry/Entity Type

Printing

Requirements
Must have
• Use the current logo and colours - see files uploaded
Limit scrolling and keep pages within view
Easy to see buttons that navigate the buyer through the site
The site is to be clear, easy to understand, free from clutter (ie.ensure white space) and have a Professional/corporate look
Easy to use Quotation forms
Imagery needs to be modern, and clean -see duskmarble site

Competitor/other websites we like and why?
I like duskmarble.example.au for its’ modern look. I like how the products are displayed in High resolution are very clean and uncluttered. You can easily find the product and access ‘get a quote’.
Calloway Print has a good layout for the quote request. Check out callowayprint.example.au
www.vendrelo.example.au are print brokers/managers. Their descriptions are easy to understand but still heavy in content.
Nice to have
• 1. Home Page
½ page summary of the core business
Distinct buttons for products and services down the side (so that people can go straight to what they need.)
About Us (including profiles); Products and Services; Get a Quote; Contact us across the top

2. About Us
A brief overview of owner, staff and reps. Click through to Profiles for each region rep and contact details either as pop ups or separate pages.

3. Products and Services
Buttons or lists of products link to pop up with get a quote link within (this could be grouped such as Business Cards, Letterheads, Folders etc.; Club printing with plastic cards, sign in books, coasters etc.; Marketing such as flyers, posters, banners etc. (Note. look at how others have broken it up)
Include calling for advice for special products and finishes as service on how a job can be improved and done within budget.
4. Get a Quote
(2 sites mentioned below that I like for the get a quote system)

5. Contact Us
Clear sections divided by lines and details large starting with 1300 number
Head office
Regional numbers and areas they cover
Include emails.

Contact us now or click to request a rep contact you.

```html
<!DOCTYPE html>
<html lang="en">
<head>
<meta charset="utf-8">
<title>Harbour Press</title>
<link href="https://fonts.googleapis.com/css2?family=Oswald:wght@300;400;500;700&family=Russo+One&family=Convergence&family=Arimo:wght@400;700&display=swap" rel="stylesheet">
<style>
:root{
  --red:#d8232a;
  --red-bright:#f03a3a;
  --nav-grey:#c9c8c6;
  --grey-text:#6a6a6a;
  --dark:#333;
  --paper:#f7f5f0;
  --band:#e3e1db;
  --white:#fff;
  --arrow:#b9b9b9;
}
*{box-sizing:border-box;margin:0;padding:0}
html,body{width:1184px;height:1200px;overflow:hidden}
body{position:relative;background:var(--paper);font-family:'Arimo',Arial,sans-serif;color:var(--dark)}
.abs{position:absolute}

/* header */
.topbar{left:0;top:0;width:1184px;height:82px;background:var(--red)}
.brand-mark{left:32px;top:6px;width:72px;height:72px;background:var(--white);border-radius:12px}
.brand-name{left:121px;top:38px;font-family:'Arimo',Arial,sans-serif;font-weight:700;font-size:36px;line-height:1;color:var(--white);letter-spacing:1px;white-space:nowrap}
.navbar{left:0;top:82px;width:1184px;height:48px;background:var(--nav-grey)}
.nav{left:34px;top:82px;height:48px;display:flex;gap:25px;align-items:center;list-style:none}
.nav li{font-family:'Oswald',sans-serif;font-weight:500;font-size:21px;color:var(--red);text-transform:uppercase;letter-spacing:-.3px;white-space:nowrap}
.contact-box{left:966px;top:10px;width:218px;height:120px;background:var(--white);border-top:3px solid var(--red)}
.contact-label{left:20px;top:14px;display:flex;align-items:center;gap:8px;font-family:'Oswald',sans-serif;font-weight:300;font-size:33px;color:var(--red);line-height:1;white-space:nowrap}
.contact-phone{left:14px;top:60px;font-family:'Oswald',sans-serif;font-weight:700;font-size:40px;color:var(--red);line-height:1;letter-spacing:-1px;white-space:nowrap;transform:scaleX(.84);transform-origin:left top}

/* hero */
.hero-photo{left:0;top:130px;width:1184px;height:486px;background:linear-gradient(180deg,#c7dbe6 0%,#d9e6ec 55%,#cfdde4 85%,#dfe6dc 100%)}
.hero-people{left:40px;top:130px;width:300px;height:486px;background:linear-gradient(180deg,#5a5f6d 0%,#3d4050 60%,#4a4d5c 100%);opacity:.35}
.hero-board{left:287px;top:239px;width:806px;height:377px;background:var(--white)}
.hero-text{left:0;top:56px;width:806px;text-align:center;font-family:'Convergence',sans-serif;font-size:26.5px;line-height:36px;color:#3a3a3a}
.quote-btn{left:255px;top:226px;width:278px;height:71px;background:var(--red-bright);border-radius:8px;color:var(--white);font-family:'Oswald',sans-serif;font-weight:500;font-size:34px;display:flex;align-items:center;justify-content:center;white-space:nowrap}
.arrow-left{left:209px;top:242px}
.arrow-right{left:549px;top:242px}

/* intro */
.intro{left:39px;top:649px;width:585px;font-size:16px;line-height:20px;color:#333}
.showcase-item{position:absolute}
.showcase-img{background:linear-gradient(135deg,#cfd3d8,#9aa3ad)}
.showcase-label{position:absolute;font-family:'Oswald',sans-serif;font-weight:400;font-size:15px;color:#333;text-transform:uppercase;letter-spacing:.3px;white-space:nowrap}

/* products */
.products-title{left:695px;top:656px;font-family:'Russo One',sans-serif;font-size:33px;color:var(--grey-text);letter-spacing:.5px;text-transform:uppercase;white-space:nowrap}
.product-list{list-style:none;top:712px}
.product-list li{position:relative;padding-left:19px;font-size:14.5px;line-height:20.5px;color:#222;white-space:nowrap}
.product-list li::before{content:"";position:absolute;left:0;top:5px;width:10px;height:10px;border-radius:50%;background:var(--red)}
.product-list li::after{content:"";position:absolute;left:3px;top:8px;border-left:4px solid var(--white);border-top:2px solid transparent;border-bottom:2px solid transparent}

/* clients */
.clients{left:0;top:914px;width:1184px;height:191px;background:var(--band)}
.client{position:absolute;top:40px;width:150px;height:94px;background:var(--white);box-shadow:0 10px 12px -8px rgba(0,0,0,.35);display:flex;align-items:center;justify-content:center;text-align:center;font-family:'Arimo',Arial,sans-serif;font-weight:700;font-size:17px;color:#333;padding:0 10px}
.carousel-arrow{position:absolute;top:64px}

/* footer */
.footer-nav{left:0;top:1131px;width:1184px;text-align:center;font-size:15px;color:#444;letter-spacing:.2px;white-space:nowrap}
.footer-nav span{margin:0 6px;color:#777}
.copyright{left:0;top:1161px;width:1184px;text-align:center;font-size:13px;color:#333;white-space:nowrap}
</style>
</head>
<body>

<header>
  <div class="abs topbar"></div>
  <div class="abs brand-mark"></div>
  <div class="abs brand-name">HARBOUR PRESS</div>
  <div class="abs navbar"></div>
  <ul class="abs nav">
    <li>Home</li><li>About Us</li><li>Products</li><li>Plastic Cards</li><li>Signage</li><li>Request a Quote</li><li>Contact Us</li><li>Blog</li>
  </ul>
  <div class="abs contact-box">
    <div class="abs contact-label">
      <svg width="34" height="34" viewBox="0 0 34 34" aria-hidden="true"><circle cx="17" cy="17" r="15" fill="none" stroke="#d8232a" stroke-width="2"/><path d="M12 9c1-1 2-1 3 0l1.5 2.5c.5 1 .3 1.8-.5 2.5l-1 1c1 2 2.5 3.5 4.5 4.5l1-1c.7-.8 1.5-1 2.5-.5L25.5 20c1 1 1 2 0 3l-1.5 1.5C20 26 9 15 10.5 10.5z" fill="#d8232a"/></svg>
      CONTACT US
    </div>
    <div class="abs contact-phone">1300 555 019</div>
  </div>
</header>

<section class="hero">
  <div class="abs hero-photo" role="img" aria-label="Three business people in suits presenting a large blank board against a pale sky"></div>
  <div class="abs hero-people" role="img" aria-label="Business people in dark suits holding the board"></div>
  <div class="abs hero-board">
    <p class="abs hero-text">From small run digital, to offset, wide-format,<br>signage, packaging, point of sale or<br>specialist hotel, retail &amp; club supplies our<br>product knowledge is second to none.</p>
    <svg class="abs arrow-left" width="31" height="40" viewBox="0 0 31 40" aria-hidden="true"><path d="M0 10h14V0l17 20-17 20V30H0z" fill="#b9b9b9"/></svg>
    <div class="abs quote-btn">REQUEST A QUOTE</div>
    <svg class="abs arrow-right" width="31" height="40" viewBox="0 0 31 40" aria-hidden="true"><path d="M31 10H17V0L0 20l17 20V30h14z" fill="#b9b9b9"/></svg>
  </div>
</section>

<section class="intro-area">
  <p class="abs intro">Using Australia's leading print trade suppliers, we provide our clients with the most cost effective print solution in the market.We are constantly sourcing the most advanced technology in the industry to produce the lowest unit price, best quality and fastest Australia wide delivery.</p>

  <div class="showcase-item" style="left:30px;top:808px">
    <div class="showcase-img" style="width:175px;height:78px;border-radius:30px 40px 10px 10px;background:linear-gradient(180deg,#f2f2f2,#cfcfcf)" role="img" aria-label="White hatchback car with printed vehicle stickers"></div>
    <span class="showcase-label" style="left:60px;top:76px">Stickers</span>
  </div>
  <div class="showcase-item" style="left:222px;top:749px">
    <div class="showcase-img" style="width:106px;height:111px;background:linear-gradient(135deg,#6f9bbf,#c23a3a)" role="img" aria-label="Two pull-up display banners"></div>
    <span class="showcase-label" style="left:14px;top:112px">Banners</span>
  </div>
  <div class="showcase-item" style="left:342px;top:767px">
    <div class="showcase-img" style="width:108px;height:78px;background:linear-gradient(135deg,#3d3d4a,#b6423a)" role="img" aria-label="Stack of full colour digital printed flyers"></div>
    <span class="showcase-label" style="left:0;top:80px">Digital Prints</span>
  </div>
  <div class="showcase-item" style="left:459px;top:809px">
    <div class="showcase-img" style="width:163px;height:78px;transform:skewY(-8deg);background:linear-gradient(135deg,#8a6a4c,#e9e1d3)" role="img" aria-label="Fanned row of printed business cards"></div>
    <span class="showcase-label" style="left:25px;top:84px">Cards</span>
  </div>

  <h2 class="abs products-title">Products and Services</h2>
  <ul class="abs product-list" style="left:698px">
    <li>Beer coasters</li><li>Brochures &amp; flyers</li><li>Carbonless books</li><li>Note pads</li><li>Presentation folders</li><li>School Yearbooks</li><li>Product boxes</li>
  </ul>
  <ul class="abs product-list" style="left:879px">
    <li>Membership cards</li><li>Retail Gift cards</li><li>VIP member cards</li><li>ID cards</li><li>Staff cards</li><li>Access cards</li><li>Student Cards</li><li>Loyalty cards</li>
  </ul>
  <ul class="abs product-list" style="left:1059px">
    <li>Posters</li><li>Signage</li><li>Banners</li><li>Stickers</li><li>Wall Sign</li>
  </ul>
</section>

<section class="abs clients">
  <svg class="carousel-arrow" style="left:10px" width="30" height="50" viewBox="0 0 30 50" aria-hidden="true"><path d="M30 0v50L0 25z" fill="#9a9a9a"/></svg>
  <div class="client" style="left:100px">Arden Rowe</div>
  <div class="client" style="left:306px">Mintleaf Yogurt</div>
  <div class="client" style="left:511px">Clearbrook Water</div>
  <div class="client" style="left:716px">Stride Fitness</div>
  <div class="client" style="left:922px">Crumb &amp; Co</div>
  <svg class="carousel-arrow" style="left:1141px" width="30" height="50" viewBox="0 0 30 50" aria-hidden="true"><path d="M0 0v50l30-25z" fill="#9a9a9a"/></svg>
</section>

<footer>
  <p class="abs footer-nav">HOME<span>·</span>ABOUT US<span>·</span>PRODUCTS<span>·</span>PLASTIC CARDS<span>·</span>SIGNAGE<span>·</span>REQUEST A QUOTE<span>·</span>BLOG<span>·</span>CONTACT</p>
  <p class="abs copyright">© Copyright Harbour Press - A Division of Coastal Buyers Collective Pty Limited</p>
</footer>

</body>
</html>
```